Landscape Contractor in need of New Web Design

HELP.. Please Help!!!!. Our current website is old, outdated, ugly... and well nothing like us.... so we are looking for someone to help build a new website that fits our company direction. We are a landscape company with multiple locations in order to meet the needs of our clients and their projects throughout the midwest. When most people think of landscaping, they think of mowing grandmas yard, but that is NOT even remotely close to what we do. We are 100% a commercial landscape company meaning we complete landscape and irrigation services for large scale commercial projects. We are looking for a website to showcase our commercial talents and awesome team of people.
Updates

Address of current website is www.plovermeadowco.com

```html
<!DOCTYPE html>
<html lang="en">
<head>
<meta charset="utf-8">
<title>Plover Meadow – Commercial Landscaping</title>
<link href="https://fonts.googleapis.com/css2?family=Outfit:wght@300;400;500;600&family=Roboto:wght@400;500&display=swap" rel="stylesheet">
<style>
:root{
  --green:#0b5c31;
  --green-deep:#074a26;
  --lime:#86c90c;
  --lime-bright:#a6e01a;
  --ink:#1d1f1c;
  --muted:#8a8f88;
  --line:#e4e6e2;
  --white:#ffffff;
  --track:#e9ebe7;
}
*{box-sizing:border-box;margin:0;padding:0}
html,body{width:1200px;height:3704px;overflow:hidden;background:var(--white)}
body{font-family:"Outfit",sans-serif;color:var(--ink)}
.page{position:relative;width:1200px;height:3704px;overflow:hidden}
.abs{position:absolute}
.small{font-family:"Roboto",sans-serif;font-size:9.5px;color:var(--muted);line-height:1.55}
.label{font-size:10px;color:var(--green);font-weight:500}
.h2{font-size:27px;font-weight:400;line-height:1.22;color:var(--ink)}
.btn{display:flex;align-items:center;justify-content:center;background:var(--lime);color:var(--green-deep);font-size:9.5px;font-weight:600;letter-spacing:1.2px;text-transform:uppercase}

/* top bar */
.topbar{top:0;left:0;width:1200px;height:39px;border-bottom:1px solid var(--line)}
.topbar .hours{left:302px;top:14px;display:flex;gap:22px;align-items:center}
.topbar .social{right:296px;top:14px;font-size:9px;color:var(--muted);display:flex;gap:10px}
/* header */
.header{top:39px;left:0;width:1200px;height:67px}
.brand{left:296px;top:24px;display:flex;align-items:center;gap:7px}
.brand .dot{width:12px;height:12px;border-radius:50%;background:var(--lime)}
.brand span{font-size:15px;font-weight:600;color:var(--green);white-space:nowrap}
.nav{font-size:10px}
.nav a{position:absolute;white-space:nowrap;color:var(--ink);text-decoration:none}
.quote{left:783px;top:14px;display:flex;gap:10px;border-left:1px solid var(--line);padding-left:10px}
.quote b{display:block;color:var(--green);font-weight:500;font-size:11px}
.quote p{font-size:9.5px;color:var(--muted);line-height:1.4}

/* hero */
.hero{top:106px;left:0;width:1200px;height:430px;background:linear-gradient(100deg,#245a18 0%,#3f7d23 35%,#5c8f2c 55%,#c86a22 72%,#3c6b1e 88%,#29521a 100%)}
.hero h1{left:296px;top:112px;font-size:44px;font-weight:400;color:var(--white);line-height:1.14}
.hero p{left:296px;top:228px;width:300px;font-family:Roboto,sans-serif;font-size:9.5px;line-height:1.55;color:#e9f2e3}
.hero .btn{left:296px;top:292px;width:109px;height:27px}

.quotebox{top:476px;left:302px;width:600px;height:129px;background:var(--white);box-shadow:0 8px 26px rgba(0,0,0,.12)}
.quotebox .call{position:absolute;left:0;top:0;width:210px;height:129px;background:var(--green);color:var(--white);text-align:center;padding-top:30px}
.call b{display:block;font-weight:400;font-size:12px;margin-top:6px}
.call span{font-size:8.5px}
.field{position:absolute;height:20px;border:1px solid var(--line);font-size:7.5px;color:var(--muted);padding:5px 7px}
.quotebox .submit{position:absolute;left:468px;top:50px;width:107px;height:20px;background:var(--green);color:var(--white);font-size:7.5px;letter-spacing:1px;font-weight:600;display:flex;align-items:center;justify-content:center}
.quotebox .note{position:absolute;left:234px;top:98px;font-size:8px;color:var(--muted)}

/* about */
.about-label{left:296px;top:815px}
.about-title{left:296px;top:836px;width:200px;line-height:32px}
.about-copy{left:296px;width:185px;font-size:8px;line-height:14px}
.badges{left:296px;top:1129px;display:flex;gap:20px}
.badges span{display:block;width:70px;height:34px;border-radius:17px;background:#e6f1dd}
.about .btn{left:296px;top:1194px;width:105px;height:29px}

.card{position:absolute;width:175px;background:var(--white);box-shadow:0 3px 16px rgba(0,0,0,.09);padding:11px 11px 16px}
.card .ph{width:153px;height:135px}
.card h3{font-size:12px;font-weight:400;margin:10px 0 6px;line-height:1.25}
.card .small{font-size:8px}
.card .more{display:block;margin-top:9px;font-size:8px;color:var(--green);font-weight:500}

/* achievement */
.achieve{top:1479px;left:0;width:1200px;height:349px;background:linear-gradient(100deg,#3b6a1e 0%,#5f8b2c 35%,#4a7c2a 55%,#2f7b7e 70%,#3d6b20 100%)}
.achieve .label{color:var(--lime-bright)}
.stat{position:absolute;top:178px;width:101px;height:95px;background:var(--white);text-align:center;padding-top:14px}
.stat b{display:block;font-size:16px;font-weight:400;color:var(--green);margin-top:4px}
.stat b sup{color:var(--lime);font-size:9px}
.stat span{font-size:8px;color:var(--green)}

/* why */
.ticks{display:grid;grid-template-columns:115px 115px;row-gap:9px;font-size:8.5px;color:var(--muted)}
.ticks li{list-style:none;display:flex;gap:5px;align-items:center}

/* process */
.process{top:2233px;left:0;width:1200px;height:411px;background:var(--green);color:var(--white);text-align:center}
.step{position:absolute;top:221px;width:150px;text-align:center}
.step h4{font-size:11px;font-weight:400;margin:12px 0 6px}
.step p{font-family:Roboto,sans-serif;font-size:8.5px;line-height:1.55;color:#cfe0d4}

/* skills */
.skill{position:absolute;left:296px;width:253px}
.skill .row{display:flex;justify-content:space-between;font-size:8.5px}
.skill .track{margin-top:5px;height:10px;background:var(--track)}
.skill .fill{height:10px;background:var(--lime)}

/* cta */
.cta{top:3048px;left:0;width:1200px;height:269px;background:linear-gradient(90deg,#244a16 0%,#39651f 40%,#2f5a1a 70%,#6f6a48 84%,#2d5618 100%);text-align:center;color:var(--white)}

/* footer */
.footer{top:3317px;left:0;width:1200px;height:387px;background:var(--green);color:var(--white)}
.footer h5{font-size:11px;font-weight:400;color:var(--lime-bright)}
.footer .small{color:#bcd3c3;font-size:8.5px}
.flinks li{list-style:none;font-family:Roboto,sans-serif;font-size:8.5px;color:#bcd3c3;margin-top:9px}
.finfo{display:flex;gap:10px;align-items:flex-start}
.finfo b{display:block;font-weight:400;color:var(--lime-bright);font-size:11px}
.finfo p{font-family:Roboto,sans-serif;font-size:8.5px;color:#dce9e0;line-height:1.5}
.footer-brand{left:296px;top:52px;display:flex;align-items:center;gap:8px}
.footer-brand .dot{width:18px;height:18px;border-radius:50%;background:var(--lime-bright)}
.footer-brand span{font-size:16px;font-weight:600;color:var(--lime-bright);white-space:nowrap}
</style>
</head>
<body>
<div class="page">

  <!-- top bar -->
  <div class="abs topbar">
    <div class="abs hours small">
      <span style="display:flex;gap:6px;align-items:center"><svg width="9" height="9"><circle cx="4.5" cy="4.5" r="4.5" fill="#0b5c31"/></svg>Mon - Sat: 8am-6pm</span>
      <span style="display:flex;gap:6px;align-items:center"><svg width="10" height="8"><rect width="10" height="8" fill="#0b5c31"/></svg>hello@plovermeadowco.com</span>
    </div>
    <div class="abs social"><span>Facebook</span><span>·</span><span>Twitter</span><span>·</span><span>Linkedin</span><span>·</span><span>Instagram</span></div>
  </div>

  <!-- header -->
  <div class="abs header">
    <div class="abs brand"><span class="dot"></span><span>Plover Meadow</span></div>
    <nav class="abs nav" style="left:0;top:28px">
      <a style="left:444px;color:#86c90c">Homepage</a>
      <a style="left:513px">Divisions ⌄</a>
      <a style="left:588px">Services ⌄</a>
      <a style="left:661px">About us</a>
      <a style="left:723px">Contact</a>
    </nav>
    <div class="abs quote">
      <svg width="22" height="22" viewBox="0 0 24 24" fill="none" stroke="#86c90c" stroke-width="1.6"><path d="M5 3h4l2 5-2.5 1.5a11 11 0 0 0 6 6L16 13l5 2v4a2 2 0 0 1-2 2A16 16 0 0 1 3 5a2 2 0 0 1 2-2z"/></svg>
      <div><b>Get Quote</b><p>(555) 201-4830<br>(555) 377-6102</p></div>
    </div>
  </div>

  <!-- hero -->
  <section class="abs hero" role="img" aria-label="Photo of a gardener in an orange cap trimming a green hedge">
    <h1 class="abs">Expert Gardener &amp;<br>Best Service.</h1>
    <p class="abs">Experts worker in landscaping and home plantations with decades of experience. Professional workers and provide the right and best solutions for you.</p>
    <div class="abs btn">Get Started</div>
  </section>

  <div class="abs quotebox">
    <div class="call">
      <svg width="28" height="28" viewBox="0 0 24 24" fill="none" stroke="#fff" stroke-width="1.3"><path d="M5 3h4l2 5-2.5 1.5a11 11 0 0 0 6 6L16 13l5 2v4a2 2 0 0 1-2 2A16 16 0 0 1 3 5a2 2 0 0 1 2-2z"/></svg>
      <b>Call Us Now</b><span>1-555-201-4830</span>
    </div>
    <div class="field" style="left:236px;top:20px;width:107px">Name</div>
    <div class="field" style="left:352px;top:20px;width:106px">Phone Number</div>
    <div class="field" style="left:468px;top:20px;width:107px">Email</div>
    <div class="field" style="left:236px;top:50px;width:107px">Select Services<span style="float:right">⌄</span></div>
    <div class="field" style="left:352px;top:50px;width:106px">Select Date</div>
    <div class="submit">GET A QUOTE</div>
    <div class="note"><b style="color:#1d1f1c">i</b>&nbsp;&nbsp; Leo vulputate orci habitant molestie semper commodo malesuada aliquam</div>
  </div>

  <!-- about -->
  <section class="about">
    <div class="abs label about-label">Who We Are</div>
    <h2 class="abs h2 about-title">We are a full service lawn and landscape contractor.</h2>
    <p class="abs small about-copy" style="top:975px">Sed ut perspiciatis unde omnis iste natus error sit voluptatem accusantium doloremque laudantium, totam rem aperiam, eaque ipsa quae ab illo inventore veritatis et quasi architecto beatae vitae dicta sunt explicabo.</p>
    <p class="abs small about-copy" style="top:1051px">Nemo enim ipsam voluptatem quia voluptas sit aspernatur aut odit aut fugit, sed quia consequuntur magni dolores eos qui ratione voluptatem sequi nesciunt.</p>
    <div class="abs badges"><span></span><span></span></div>
    <div class="abs btn">Learn More</div>

    <div class="card" style="left:526px;top:657px"><div class="ph" role="img" aria-label="Gardener trimming a hedge with shears" style="background:linear-gradient(135deg,#4f8a2a,#a07a3c)"></div><h3>Maintenance</h3><p class="small">Sed ut perspiciatis unde omnis iste natus error sit voluptatem.</p><span class="more">Read More</span></div>
    <div class="card" style="left:717px;top:678px"><div class="ph" role="img" aria-label="Gardener tending shrubs" style="background:linear-gradient(135deg,#4f8a2a,#9c7a3e)"></div><h3>Chemical Applications &amp; Fertilization</h3><p class="small">Sed ut perspiciatis unde omnis iste natus error sit voluptatem.</p><span class="more">Read More</span></div>
    <div class="card" style="left:526px;top:912px"><div class="ph" role="img" aria-label="Aerial view of turf rolls laid beside a pool" style="background:linear-gradient(135deg,#35b4c8,#6aa04a)"></div><h3>Turf Management</h3><p class="small">Sed ut perspiciatis unde omnis iste natus error sit voluptatem.</p><span class="more">Read More</span></div>
    <div class="card" style="left:717px;top:948px"><div class="ph" role="img" aria-label="Stone path through a garden" style="height:115px;background:linear-gradient(135deg,#4d5a3a,#8f8470)"></div><h3>Hardscaping</h3><p class="small">Sed ut perspiciatis unde omnis iste natus error sit voluptatem.</p><span class="more">Read More</span></div>
    <div class="card" style="left:526px;top:1168px"><div class="ph" role="img" aria-label="Drip irrigation hose laid in a garden bed" style="background:linear-gradient(135deg,#5a8a3a,#6c6f70)"></div><h3>Irrigation</h3><p class="small">Sed ut perspiciatis unde omnis iste natus error sit voluptatem.</p><span class="more">Read More</span></div>
    <div class="card" style="left:717px;top:1185px"><div class="ph" role="img" aria-label="Gardener in blue cap planting red flowers" style="background:linear-gradient(135deg,#3f7a2a,#2f8fb8)"></div><h3>Landscaping</h3><p class="small">Sed ut perspiciatis unde omnis iste natus error sit voluptatem.</p><span class="more">Read More</span></div>
  </section>

  <!-- achievement -->
  <section class="abs achieve" role="img" aria-label="Photo of a gardener in a blue cap working outdoors among greenery">
    <div class="abs label" style="left:296px;top:52px">The Fact</div>
    <h2 class="abs h2" style="left:296px;top:77px;color:#fff">The Achivement</h2>
    <p class="abs small" style="left:296px;top:122px;width:336px;color:#e3eedc;font-size:8.5px">Sed ut perspiciatis unde omnis iste natus error sit voluptatem accusantium doloremque laudantium, totam rem aperiam, eaque ipsa quae ab illo inventore veritatis et quasi architecto beatae vitae dicta.</p>
    <div class="stat" style="left:296px"><svg width="26" height="26" viewBox="0 0 24 24" fill="none" stroke="#86c90c" stroke-width="1.3"><circle cx="12" cy="10" r="5"/><path d="M5 21h14M12 15v6"/></svg><b>150 <sup>+</sup></b><span>Finished Projects</span></div>
    <div class="stat" style="left:414px"><svg width="26" height="26" viewBox="0 0 24 24" fill="none" stroke="#86c90c" stroke-width="1.3"><circle cx="12" cy="8" r="4"/><path d="M4 21c0-5 4-7 8-7s8 2 8 7z"/></svg><b>100 <sup>+</sup></b><span>Professional Team</span></div>
    <div class="stat" style="left:530px"><svg width="26" height="26" viewBox="0 0 24 24" fill="none" stroke="#86c90c" stroke-width="1.3"><circle cx="12" cy="8" r="4"/><path d="M4 21c0-5 4-7 8-7s8 2 8 7"/></svg><b>120 <sup>+</sup></b><span>Happy Customer</span></div>
  </section>

  <!-- why choose -->
  <div class="abs" role="img" aria-label="Gardener in orange cap with a green lawn mower" style="left:296px;top:1883px;width:306px;height:393px;background:linear-gradient(180deg,#4aa0d8 0%,#c9b640 45%,#3c8a2a 100%)"></div>
  <div class="abs" style="left:651px;top:1930px;width:250px">
    <div class="label">Why Choose Us</div>
    <h2 class="h2" style="font-size:22px;margin:10px 0 12px">15 year of Professional landscaping</h2>
    <p class="small" style="font-size:8.5px">We Design, Build and Maintain Residential and Commercial Landscapes.</p>
    <ul class="ticks" style="margin-top:18px">
      <li><span style="color:#86c90c">✔</span>Residential</li><li><span style="color:#86c90c">✔</span>Municipality</li>
      <li><span style="color:#86c90c">✔</span>Commercial</li><li><span style="color:#86c90c">✔</span>Sports fields</li>
      <li><span style="color:#86c90c">✔</span>Government</li>
    </ul>
  </div>
  <div class="abs btn" style="left:651px;top:2135px;width:105px;height:28px">Learn More</div>

  <!-- process -->
  <section class="abs process">
    <div class="label" style="color:#a6e01a;margin-top:88px">The Process</div>
    <h2 class="h2" style="color:#fff;font-size:22px;margin-top:8px">Our Work Process</h2>
    <p style="font-family:Roboto,sans-serif;font-size:9px;color:#d6e5db;line-height:1.7;margin-top:16px">Sed ut perspiciatis unde omnis iste natus error sit voluptatem<br>accusantium doloremque laudantium, totam rem aperiam.</p>
    <div class="step" style="left:329px"><svg width="36" height="36" viewBox="0 0 24 24" fill="none" stroke="#a6e01a" stroke-width="1.1"><rect x="3" y="3" width="18" height="11"/><circle cx="8" cy="17" r="2"/><circle cx="16" cy="17" r="2"/><path d="M6 7h8M6 10h5"/></svg><h4>Project Discusion</h4><p>Sed ut perspiciatis<br>unde omnis iste natus.</p></div>
    <div class="step" style="left:526px"><svg width="36" height="36" viewBox="0 0 24 24" fill="none" stroke="#a6e01a" stroke-width="1.1"><rect x="5" y="2" width="14" height="20"/><circle cx="12" cy="8" r="3"/><path d="M8 19v-3M11 19v-5M14 19v-4M17 19v-6"/></svg><h4>Project Planning</h4><p>Sed ut perspiciatis<br>unde omnis iste natus.</p></div>
    <div class="step" style="left:724px"><svg width="36" height="36" viewBox="0 0 24 24" fill="none" stroke="#a6e01a" stroke-width="1.1"><path d="M4 13a8 8 0 0 1 16 0z"/><path d="M10 5v8M14 5v8M3 13h18"/><rect x="5" y="16" width="14" height="4" rx="2"/></svg><h4>Project Execution</h4><p>Sed ut perspiciatis<br>unde omnis iste natus.</p></div>
    <svg class="abs" style="left:466px;top:248px" width="76" height="24" viewBox="0 0 76 24" fill="none" stroke="#fff" stroke-width="3"><path d="M2 18Q36 2 70 12"/><path d="M60 4l11 8-12 6"/></svg>
    <svg class="abs" style="left:662px;top:248px" width="76" height="24" viewBox="0 0 76 24" fill="none" stroke="#fff" stroke-width="3"><path d="M2 18Q36 2 70 12"/><path d="M60 4l11 8-12 6"/></svg>
  </section>

  <!-- skills -->
  <div class="abs" role="img" aria-label="Gardener in blue cap pruning a bonsai pine" style="left:602px;top:2598px;width:306px;height:395px;background:linear-gradient(160deg,#e7ead6 0%,#5f9a32 40%,#2b8fa8 70%,#4d8a2a 100%)"></div>
  <div class="abs" style="left:296px;top:2719px;width:260px">
    <div class="label">The Value</div>
    <h2 class="h2" style="font-size:22px;margin:10px 0 12px">Our Team Best Skill to Service</h2>
    <p class="small" style="font-size:8.5px">Sed ut perspiciatis unde omnis iste natus error sit voluptatem accusantium doloremque laudantium, totam rem aperiam.</p>
  </div>
  <div class="skill" style="top:2846px"><div class="row" style="width:227px"><span>Landscaping</span><span>90%</span></div><div class="track"><div class="fill" style="width:90%"></div></div></div>
  <div class="skill" style="top:2885px"><div class="row" style="width:202px"><span>Gardening</span><span>80%</span></div><div class="track"><div class="fill" style="width:80%"></div></div></div>
  <div class="skill" style="top:2924px"><div class="row" style="width:177px"><span>Decorating</span><span>70%</span></div><div class="track"><div class="fill" style="width:70%"></div></div></div>

  <!-- call to action -->
  <section class="abs cta" role="img" aria-label="Aerial view of a garden with a winding path">
    <h2 class="h2" style="color:#fff;font-size:22px;margin-top:80px">Let's Begin A New Project with Us</h2>
    <p style="font-family:Roboto,sans-serif;font-size:8.5px;line-height:1.7;color:#e1ecd9;margin-top:10px">Sed ut perspiciatis unde omnis iste natus error sit voluptatem<br>accusantium doloremque laudantium, totam rem aperiam</p>
    <div class="btn" style="width:100px;height:29px;margin:12px auto 0">Learn More</div>
  </section>

  <!-- footer -->
  <footer class="abs footer">
    <div class="abs footer-brand"><span class="dot"></span><span>Plover Meadow</span></div>
    <div class="abs finfo" style="left:451px;top:63px">
      <svg width="18" height="18" viewBox="0 0 24 24" fill="none" stroke="#a6e01a" stroke-width="1.4"><path d="M5 3h4l2 5-2.5 1.5a11 11 0 0 0 6 6L16 13l5 2v4a2 2 0 0 1-2 2A16 16 0 0 1 3 5a2 2 0 0 1 2-2z"/></svg>
      <div><b>Phone</b><p>(555) 201-4830<br>(555) 377-6102</p></div>
    </div>
    <div class="abs finfo" style="left:585px;top:68px">
      <svg width="18" height="14" viewBox="0 0 24 18" fill="none" stroke="#a6e01a" stroke-width="1.4"><rect x="1" y="1" width="22" height="16"/><path d="M1 1l11 9 11-9"/></svg>
      <div><b>Mail</b><p>hello@plovermeadowco.com</p></div>
    </div>
    <div class="abs finfo" style="left:755px;top:38px">
      <svg width="18" height="16" viewBox="0 0 24 20" fill="none" stroke="#a6e01a" stroke-width="1.4"><path d="M1 3l7-2 8 2 7-2v16l-7 2-8-2-7 2zM8 1v16M16 3v16"/></svg>
      <div><b>Location</b><p>418 Fenwick Lane,<br>Alder Falls, KS 66012</p></div>
    </div>
    <div class="abs finfo" style="left:755px;top:94px">
      <svg width="18" height="16" viewBox="0 0 24 20" fill="none" stroke="#a6e01a" stroke-width="1.4"><path d="M1 3l7-2 8 2 7-2v16l-7 2-8-2-7 2zM8 1v16M16 3v16"/></svg>
      <div><b>Location</b><p>9020 W 54th Court,<br>Birch Hollow, KS 66310</p></div>
    </div>

    <div class="abs" style="left:296px;top:187px;width:160px">
      <h5>About Us</h5>
      <p class="small" style="margin-top:10px">Sed ut perspiciatis unde omnis iste natus error sit voluptatem accusantium doloremque laudanti totam rem aperiam inventore veritatis</p>
      <div style="display:flex;gap:14px;margin-top:18px;padding-left:8px">
        <span style="width:8px;height:8px;border-radius:50%;background:#a6e01a"></span><span style="width:8px;height:8px;border-radius:50%;background:#a6e01a"></span><span style="width:8px;height:8px;border-radius:50%;background:#a6e01a"></span><span style="width:8px;height:8px;border-radius:50%;background:#a6e01a"></span>
      </div>
    </div>
    <div class="abs" style="left:484px;top:187px"><h5>Quick Links</h5><ul class="flinks"><li>About Us</li><li>Services</li><li>Projects</li><li>Contact</li></ul></div>
    <div class="abs" style="left:589px;top:187px"><h5>Useful Links</h5><ul class="flinks"><li>Privacy Policy</li><li>Terms and Conditions</li><li>Disclaimer</li><li>Support</li></ul></div>
    <div class="abs" style="left:710px;top:187px;width:198px">
      <h5>News letter</h5>
      <p class="small" style="margin-top:10px">Sed ut perspiciatis unde omnis iste natus error sit voluptatem accusantium</p>
      <div style="display:flex;margin-top:36px;height:25px">
        <div style="flex:1;background:#fff;font-size:7px;color:#aaa;padding:8px 10px;font-family:Roboto,sans-serif">Your Email Address</div>
        <div style="width:30px;background:#86c90c;display:flex;align-items:center;justify-content:center"><svg width="11" height="11" viewBox="0 0 24 24" fill="#fff"><path d="M2 12l20-9-7 20-3-8z"/></svg></div>
      </div>
    </div>
    <div class="abs" style="left:296px;top:344px;width:612px;border-top:1px solid rgba(255,255,255,.12)"></div>
    <p class="abs small" style="left:296px;top:360px;font-size:8px">Copyright © Your company 2021. All Right Reserved.</p>
  </footer>
</div>
</body>
</html>
```